Educational clinic needs a new webpage design

I have a relatively new website but I am unhappy with the design. I was hoping the look of it would more match my logo, brochures, business cards, and postcards. The content is good and it's already mobile ready. The designer used square space, which I would like to keep if possible. My website is www.harborlightstudyhouse.example

Target Market(s)

Parents of school age children

Industry/Entity Type

Education

Number of Pages Required

5+ page

Requirements
Must have
• Pictures must depict the diversity of our students. We service all ages, from preschool through college and our students come from varying races.
Should not have
• I try to avoid the word "tutoring" because what we do is so much more. I like the tag line of "results that go beyond traditional tutoring"

```html
<!DOCTYPE html>
<html lang="en">
<head>
<meta charset="utf-8">
<title>Harborlight Study House</title>
<link href="https://fonts.googleapis.com/css2?family=Open+Sans:wght@400;600;700&family=Roboto:wght@400;500;700&family=Ubuntu:wght@400;500;700&display=swap" rel="stylesheet">
<style>
:root{
  --purple:#6a2d8f;
  --purple-dark:#4f1f73;
  --purple-title:#52238a;
  --green:#8cc63f;
  --green-soft:#b9d874;
  --ink:#222;
  --body:#444;
  --grey-bg:#ececec;
  --dark:#1e1e1e;
  --field:#e4d6ec;
}
*{box-sizing:border-box;margin:0;padding:0}
html,body{width:1200px;height:2699px;overflow:hidden}
body{position:relative;font-family:"Open Sans",sans-serif;color:var(--body);background:#fff}
.abs{position:absolute}

/* header */
.site-header{left:0;top:0;width:1200px;height:122px;background:#fff}
.brand{left:100px;top:30px;display:flex;align-items:center;gap:16px}
.brand-dot{width:62px;height:62px;border-radius:50%;background:var(--purple)}
.brand-name{font-family:"Roboto",sans-serif;font-weight:700;font-size:30px;color:var(--purple);line-height:1}
.contact-top{left:815px;top:36px;font-size:15px;color:var(--ink);line-height:38px}
.contact-top div{display:flex;align-items:center;gap:10px}
.ic{width:22px;height:22px;border-radius:50%;border:2px solid var(--green);display:inline-flex;align-items:center;justify-content:center}

/* nav */
.main-nav{left:0;top:122px;width:1200px;height:40px;background:var(--purple)}
.main-nav ul{list-style:none;display:flex;position:absolute;left:102px;top:0;height:40px;align-items:center}
.main-nav li{color:#fff;font-size:16px;padding:0 22px;border-left:1px solid rgba(255,255,255,.35)}
.main-nav li:first-child{padding-left:2px;border:0;font-weight:600;text-decoration:underline;text-underline-offset:5px}
.search{left:845px;top:127px;width:256px;height:30px;background:#fff;display:flex}
.search span{flex:1;font-size:11px;font-style:italic;color:#888;padding:8px 8px}
.search b{width:30px;background:var(--green);display:flex;align-items:center;justify-content:center}

/* hero */
.hero-band{left:0;top:162px;width:1200px;height:414px;background:linear-gradient(180deg,#2b2b2b,#111)}
.grey-area{left:0;top:576px;width:1200px;height:504px;background:var(--grey-bg)}
.slide{left:99px;top:212px;width:1001px;height:436px;background:#fff;border:5px solid #fff;box-shadow:0 6px 14px rgba(0,0,0,.25);overflow:hidden}
.slide-photo{left:0;top:0;width:560px;height:426px;background:linear-gradient(135deg,#f3f3f3,#d9d2c4 55%,#bfb3a0)}
.slide-panel{left:0;top:0}
.slide-copy{left:580px;top:60px;width:400px;text-align:center;color:#fff;font-family:"Ubuntu",sans-serif}
.slide-copy .mark{width:74px;height:74px;border-radius:50%;background:rgba(255,255,255,.55);margin:0 auto 40px}
.slide-copy p{font-size:24px}
.slide-copy h1{font-size:36px;font-weight:700;letter-spacing:1px;margin:12px 0 20px}
.btn-green{display:inline-block;background:var(--green);color:#fff;font-size:16px;padding:8px 16px;border-radius:2px}
.arrow{top:412px;width:28px;height:42px;background:#111;display:flex;align-items:center;justify-content:center}

/* cards */
.card{top:705px;width:308px;height:317px;background:#fff;text-align:center}
.card-photo{height:162px;width:100%}
.card-dot{width:44px;height:44px;border-radius:50%;background:#fff;margin:-24px auto 0;position:relative;display:flex;align-items:center;justify-content:center}
.card-dot i{width:26px;height:26px;border-radius:50%;background:var(--purple)}
.card h3{font-family:"Ubuntu",sans-serif;font-size:21px;font-weight:500;color:var(--ink);margin:6px 0 10px}
.card p{font-size:12px;line-height:19px;padding:0 26px;color:#333}
.plus{position:absolute;left:50%;bottom:-10px;margin-left:-14px;width:28px;height:24px;background:var(--purple);color:#fff;font-weight:700;line-height:24px}

/* about */
.about{left:0;top:1080px;width:1200px;height:381px;background:#fff;text-align:center}
.sec-title{font-family:"Roboto",sans-serif;font-weight:500;font-size:29px;color:var(--purple-title)}
.divider{position:relative;width:590px;height:20px;margin:8px auto 14px}
.divider:before{content:"";position:absolute;left:0;right:0;top:10px;border-top:1px solid #bbb}
.divider i{position:absolute;left:50%;top:0;margin-left:-14px;width:28px;height:22px;background:#fff}
.divider i:after{content:"";position:absolute;left:5px;top:2px;width:18px;height:18px;border-radius:50%;background:var(--purple)}
.about .lead{font-size:20px;line-height:32px;color:var(--ink);width:1010px;margin:0 auto}
.about .small{font-size:14px;line-height:24px;color:#333;width:1010px;margin:10px auto 0}
.btn-outline{display:inline-block;margin-top:24px;border:2px solid var(--purple);color:var(--purple);font-size:16px;padding:5px 12px}

/* mission */
.mission{left:0;top:1461px;width:1200px;height:297px;background:linear-gradient(90deg,#6b3a86 0%,#7d4a96 40%,#c7aed0 58%,#efe5dc 70%,#e8c9a4 100%)}
.mission-photo{left:560px;top:0;width:640px;height:297px;background:linear-gradient(90deg,rgba(235,215,200,0),#e7c7a2 35%,#d98d58 70%,#e9d6c0)}
.mission-copy{left:100px;top:36px;width:430px;color:#fff}
.mission-copy h2{font-family:"Roboto",sans-serif;font-weight:500;font-size:29px;padding-bottom:14px;border-bottom:1px solid rgba(255,255,255,.45);margin-bottom:16px}
.mission-copy p{font-size:14px;line-height:22px}
.mission-copy li{list-style:none;font-size:14px;font-weight:700;margin-top:14px;display:flex;gap:10px;align-items:center}

/* testimonials */
.testimonials{left:0;top:1758px;width:1200px;height:467px;background:#fff;text-align:center}
.testimonials h2{font-family:"Roboto",sans-serif;font-weight:500;font-size:29px;color:var(--purple-title);margin-top:52px}
.ghost{position:absolute;left:0;right:0;top:92px;font-family:"Roboto",sans-serif;font-weight:700;font-size:34px;color:#eee;letter-spacing:1px}
.sub{position:relative;font-family:"Roboto",sans-serif;font-weight:700;font-size:12px;color:var(--ink)}
.bubble{left:322px;top:183px;width:556px;height:140px;background:var(--green-soft);border-radius:46px;color:#fff;font-size:12.5px;line-height:21px;text-align:left;padding:24px 40px 0 78px}
.bubble:after{content:"";position:absolute;left:390px;bottom:-18px;border:12px solid transparent;border-top:14px solid var(--green-soft);border-bottom:0}
.quote{left:26px;top:14px;font-family:Georgia,serif;font-size:70px;color:rgba(255,255,255,.6);line-height:1}
.people{left:270px;top:340px;width:680px;height:60px}
.nav-c{position:absolute;top:10px;width:42px;height:42px;border-radius:50%;background:#e9e9e9;display:flex;align-items:center;justify-content:center}
.person{position:absolute;top:4px;display:flex;align-items:center;gap:10px;text-align:left;font-size:12px}
.avatar{width:52px;height:52px;border-radius:50%;background:linear-gradient(#c9c1b8,#8d8379)}
.person b{display:block;color:#999;font-size:12.5px}
.person span{color:#aaa;font-size:11.5px}
.person.active b{color:var(--green)}
.person.active span{color:#666}

/* footer */
.footer{left:0;top:2225px;width:1200px;height:429px;background:var(--purple);overflow:hidden}
.footer svg{position:absolute;left:0;top:0}
.foot-contact{left:102px;top:24px;color:#333;font-size:14px;line-height:21px}
.foot-contact h3{font-family:"Roboto",sans-serif;font-weight:500;font-size:21px;color:var(--purple);margin-bottom:14px}
.foot-contact .row{display:flex;align-items:center;gap:8px;margin-top:14px;font-size:13px}
.social{display:flex;gap:10px;margin-top:62px}
.social i{width:26px;height:26px;border-radius:50%;border:2px solid #ccc;background:#2e6db0}
.foot-nav{left:655px;top:22px;display:flex;gap:26px;color:#fff;font-family:"Ubuntu",sans-serif;font-weight:500;font-size:15px}
.inquiry{left:652px;top:76px;width:372px}
.inquiry h3{font-family:"Ubuntu",sans-serif;font-weight:500;color:#fff;font-size:23px;margin-bottom:12px}
.field{background:var(--field);height:40px;margin-bottom:11px;font-size:12px;color:#555;padding:13px 14px}
.field.msg{height:72px}
.btn-submit{display:inline-block;background:var(--green);color:#fff;font-weight:700;font-size:15px;padding:7px 22px}
.foot-mark{left:478px;top:268px;width:140px;height:140px;border-radius:50%;background:rgba(255,255,255,.12)}
.copyright{left:0;top:2654px;width:1200px;height:45px;background:#2a2a2a;color:#eee;font-size:13px;text-align:center;line-height:45px}
</style>
</head>
<body>

<header class="site-header abs">
  <div class="brand abs"><span class="brand-dot"></span><span class="brand-name">Harborlight Study House</span></div>
  <div class="contact-top abs">
    <div><span class="ic"><svg width="10" height="10" viewBox="0 0 24 24"><path fill="#8cc63f" d="M6.6 10.8a15 15 0 0 0 6.6 6.6l2.2-2.2c.3-.3.7-.4 1-.2 1.1.4 2.3.6 3.6.6.6 0 1 .4 1 1V20c0 .6-.4 1-1 1A17 17 0 0 1 3 4c0-.6.4-1 1-1h3.5c.6 0 1 .4 1 1 0 1.3.2 2.5.6 3.6.1.3 0 .7-.2 1z"/></svg></span>555-014-2290</div>
    <div><span class="ic"><svg width="11" height="9" viewBox="0 0 22 16"><rect x="1" y="1" width="20" height="14" fill="none" stroke="#8cc63f" stroke-width="2"/><path d="M1 1l10 8 10-8" fill="none" stroke="#8cc63f" stroke-width="2"/></svg></span>info@harborlightstudyhouse.example</div>
  </div>
</header>

<nav class="main-nav abs">
  <ul><li>Home</li><li>Services</li><li>About Us</li><li>Payments</li><li>Contact Us</li></ul>
</nav>
<div class="search abs"><span>search here</span><b><svg width="14" height="14" viewBox="0 0 24 24"><circle cx="10" cy="10" r="7" fill="none" stroke="#fff" stroke-width="3"/><path d="M15 15l7 7" stroke="#fff" stroke-width="3"/></svg></b></div>

<section class="hero-band abs"></section>
<div class="grey-area abs"></div>

<div class="slide abs">
  <div class="slide-photo abs" role="img" aria-label="Photo of four smiling schoolchildren from diverse backgrounds holding books"></div>
  <svg class="slide-panel abs" width="991" height="426" viewBox="0 0 991 426">
    <path d="M560 0 H991 V426 H180 C360 380 500 260 560 0 Z" fill="#6a2d8f"/>
    <path d="M520 0 H545 C510 250 380 370 140 426 H90 C330 370 470 250 520 0 Z" fill="#8cc63f"/>
    <path d="M545 0 H575 C540 250 400 380 180 426 H140 C380 370 510 250 545 0 Z" fill="#fff"/>
  </svg>
  <div class="slide-copy abs">
    <div class="mark"></div>
    <p>Results that go</p>
    <h1>BEYOND TUTORING</h1>
    <span class="btn-green">Contact Now!</span>
  </div>
</div>
<div class="arrow abs" style="left:88px"><svg width="10" height="16" viewBox="0 0 10 16"><path d="M8 2L2 8l6 6" stroke="#fff" stroke-width="2.5" fill="none"/></svg></div>
<div class="arrow abs" style="left:1082px"><svg width="10" height="16" viewBox="0 0 10 16"><path d="M2 2l6 6-6 6" stroke="#fff" stroke-width="2.5" fill="none"/></svg></div>

<article class="card abs" style="left:99px">
  <div class="card-photo" role="img" aria-label="Photo of cheering children raising their hands" style="background:linear-gradient(135deg,#e8d3b8,#d86a4a 50%,#4a7ac0)"></div>
  <div class="card-dot"><i></i></div>
  <h3>Our Services</h3>
  <p>Find out about our services, our methods, and the results of over a decade of tutoring.</p>
  <span class="plus">+</span>
</article>
<article class="card abs" style="left:446px">
  <div class="card-photo" role="img" aria-label="Photo of a person working at a laptop" style="background:linear-gradient(135deg,#9a9a9a,#555 50%,#cfcfcf)"></div>
  <div class="card-dot"><i></i></div>
  <h3>What We Do</h3>
  <p>Since 2004, we have been helping families with their educational needs. We are more than passionate about students' success.</p>
  <span class="plus">+</span>
</article>
<article class="card abs" style="left:792px">
  <div class="card-photo" role="img" aria-label="Photo of a hand holding a phone near a keyboard" style="background:linear-gradient(135deg,#d6dbe0,#eacbb3 50%,#b7c1ca)"></div>
  <div class="card-dot"><i></i></div>
  <h3>Contact Us</h3>
  <p>Are you ready to get your student confident in class? We are here to help you today!</p>
  <span class="plus">+</span>
</article>

<section class="about abs">
  <h2 class="sec-title" style="margin-top:46px">ABOUT HARBORLIGHT STUDY HOUSE</h2>
  <div class="divider"><i></i></div>
  <p class="lead">Lorem ipsum dolor sit amet, consectetuer adipiscing elit, sed diam nonummy nibh euismod tincidunt ut laoreet dolore magna aliquam erat volutpat. Ut wisi enim ad minim veniam, quis nostrud exerci</p>
  <p class="small">Ut wisi enim ad minim veniam, quis nostrudk exerci tation more ullamcorper suscipit lobortis nis ut aliquip commodo conseqti. Duis autem iriure dolor in hendrerit in vulputate veesseml molestie consequat, vel illum facilisi. Lorem ipsum dolor sit amet, conse ctetuer adipiscing elit, sedmoi di nonummy nibh commodo consequat. Duis autem vel eum iriurel dolor in hendrerit.</p>
  <span class="btn-outline">Read More</span>
</section>

<section class="mission abs">
  <div class="mission-photo abs" role="img" aria-label="Photo of smiling children with backpacks in a school hallway"></div>
  <div class="mission-copy abs">
    <h2>OUR MISSION</h2>
    <p>Ut wisi enim adi minim veniam, quis nostrudk exerci tation more ullamcorper suscipit lobortis nis ut aliquip commodo conseqti duis autemiriure dolor in hendrerit in vulputate veesseml nibh vulputate veesseml molestie consequat, vel illum facilisi.</p>
    <ul>
      <li><svg width="14" height="14" viewBox="0 0 14 14"><rect x="1" y="1" width="12" height="12" fill="none" stroke="#fff" stroke-width="1.5"/><path d="M3 7l3 3 5-6" stroke="#fff" stroke-width="2" fill="none"/></svg>Dolor in hendrerit in vulputate veesseml molestie consequat</li>
      <li><svg width="14" height="14" viewBox="0 0 14 14"><rect x="1" y="1" width="12" height="12" fill="none" stroke="#fff" stroke-width="1.5"/><path d="M3 7l3 3 5-6" stroke="#fff" stroke-width="2" fill="none"/></svg>Ut wisi enim adi minim veniam, quis nostrudk exerci tation</li>
    </ul>
  </div>
</section>

<section class="testimonials abs">
  <h2>TESTIMONIALS</h2>
  <div class="ghost">WHAT PARENTS SAY ABOUT US</div>
  <div class="sub">WHAT PARENTS SAY ABOUT US</div>
  <div class="bubble abs"><span class="quote abs">&ldquo;</span>Nam eros ante, rutrum a laoreef sociosqu ad litora torquent per conubia nostra. Class aptent taciti sociosqu ad litora torquent per conubia nostra, per inceptos himenaeos. Nam eros ante, rutrum a laoreef sociosqu ad litora torquent per conubia nostra</div>
  <div class="people abs">
    <span class="nav-c" style="left:3px"><svg width="10" height="14" viewBox="0 0 10 14"><path d="M8 1L2 7l6 6" stroke="#fff" stroke-width="2.5" fill="none"/></svg></span>
    <div class="person" style="left:90px"><span class="avatar"></span><div><b>Darren Pike</b><span>Peter's Father</span></div></div>
    <div class="person" style="left:262px"><span class="avatar"></span><div><b>Lena Marlowe</b><span>Peter's Mother</span></div></div>
    <div class="person active" style="left:428px"><span class="avatar"></span><div><b>Darren Pike</b><span>Peter's Father</span></div></div>
    <span class="nav-c" style="left:631px"><svg width="10" height="14" viewBox="0 0 10 14"><path d="M2 1l6 6-6 6" stroke="#fff" stroke-width="2.5" fill="none"/></svg></span>
  </div>
</section>

<footer class="footer abs">
  <svg width="1200" height="429" viewBox="0 0 1200 429">
    <path d="M0 0 H340 C470 140 430 330 90 429 H0 Z" fill="#f2f2f2"/>
    <path d="M340 0 H400 C540 150 480 340 150 429 H90 C430 330 470 140 340 0 Z" fill="#6a2d8f"/>
    <path d="M400 0 H440 C590 150 530 350 200 429 H150 C480 340 540 150 400 0 Z" fill="#fff"/>
    <path d="M440 0 H490 C640 160 570 350 260 429 H200 C530 350 590 150 440 0 Z" fill="#8cc63f"/>
    <path d="M490 0 H510 C660 160 590 360 300 429 H260 C570 350 640 160 490 0 Z" fill="#fff"/>
    <line x1="560" y1="82" x2="1200" y2="82" stroke="rgba(255,255,255,.15)"/>
  </svg>
  <div class="foot-mark abs"></div>
  <div class="foot-contact abs">
    <h3>Contact Details</h3>
    <div>Harborlight Study House</div>
    <div>123, Ut wisi enim ad minim veniam,<br>Mor nostmi tation -123 456</div>
    <div class="row"><svg width="13" height="13" viewBox="0 0 24 24"><path fill="#8cc63f" d="M6.6 10.8a15 15 0 0 0 6.6 6.6l2.2-2.2c.3-.3.7-.4 1-.2 1.1.4 2.3.6 3.6.6.6 0 1 .4 1 1V20c0 .6-.4 1-1 1A17 17 0 0 1 3 4c0-.6.4-1 1-1h3.5c.6 0 1 .4 1 1 0 1.3.2 2.5.6 3.6.1.3 0 .7-.2 1z"/></svg>(555) 014 7731</div>
    <div class="row"><svg width="13" height="10" viewBox="0 0 22 16"><rect x="0" y="0" width="22" height="16" fill="#8cc63f"/><path d="M1 1l10 8 10-8" fill="none" stroke="#fff" stroke-width="2"/></svg>info@harborlightstudyhouse.example</div>
    <div class="social"><i></i><i></i><i style="background:#3aa0e0"></i></div>
  </div>
  <div class="foot-nav abs"><span>Home</span><span>Services</span><span>About Us</span><span>Payments</span><span>Contact Us</span></div>
  <div class="inquiry abs">
    <h3>QUICK INQUIRY</h3>
    <div class="field">Name</div>
    <div class="field">Phone Number</div>
    <div class="field">Email Address</div>
    <div class="field msg">Message</div>
    <span class="btn-submit">SUBMIT</span>
  </div>
</footer>
<div class="copyright abs">Copyright &copy; 2016 Harborlight Study House. All Rights Reserved.</div>

</body>
</html>
```